Surviving Domestic Violence Flyer

I need a flyer that "POPS" to attract participants for my research project. I have added the important information on my draft flyer.

```html
<!DOCTYPE html>
<html lang="en">
<head>
<meta charset="utf-8">
<title>Request for Study Participants</title>
<link rel="stylesheet" href="https://fonts.googleapis.com/css2?family=Big+Shoulders+Stencil+Display:wght@900&family=Open+Sans:wght@800&family=Arimo:wght@400&display=swap">
<style>
  :root {
    --ink-black: #000000;
    --headline-yellow: #f4ec1a;
    --link-yellow: #f2e61c;
    --text-white: #ffffff;
    --band-top: #b8d63a;
    --band-mid: #94c03a;
    --band-bottom: #5b8a2f;
    --band-edge: #d6ec6a;
    --bullet-ink: #1f1f1f;
    --photo-light: #9a9a9a;
    --photo-dark: #2a2a2a;
  }
  * { margin: 0; padding: 0; box-sizing: border-box; }
  html, body { width: 900px; height: 1200px; overflow: hidden; background: var(--ink-black); }
  .flyer {
    position: relative;
    width: 900px;
    height: 1200px;
    background: var(--ink-black);
    font-family: "Arimo", Arial, sans-serif;
    color: var(--text-white);
  }
  .hero { position: absolute; left: 0; top: 0; width: 900px; height: 348px; }
  .hero-portrait {
    position: absolute; left: 0; top: 0; width: 340px; height: 348px;
    background:
      linear-gradient(90deg, rgba(0,0,0,0) 55%, var(--ink-black) 100%),
      radial-gradient(ellipse at 35% 55%, var(--photo-light) 0%, #666 40%, var(--photo-dark) 80%);
  }
  .headline {
    position: absolute; left: 300px; top: 80px; width: 590px;
    text-align: center;
    white-space: nowrap;
    font-family: "Big Shoulders Stencil Display", Impact, sans-serif;
    font-weight: 900;
    font-size: 62px; line-height: 66px; letter-spacing: 2px;
    color: var(--headline-yellow);
  }
  .study-title {
    position: absolute; left: 290px; top: 228px; width: 600px;
    text-align: center;
    font-size: 19px; line-height: 25px;
    color: var(--text-white);
  }
  .criteria-band {
    position: absolute; left: 0; top: 348px; width: 900px; height: 418px;
    background: linear-gradient(180deg, var(--band-top) 0%, var(--band-mid) 45%, var(--band-bottom) 100%);
    border-top: 2px solid var(--band-edge);
  }
  .criteria-list {
    position: absolute; left: 52px; top: 74px; width: 820px;
    list-style: none;
    font-family: "Open Sans", Arial, sans-serif;
    font-weight: 800; font-size: 24px; line-height: 28px;
    color: var(--bullet-ink);
  }
  .criteria-list li { position: relative; padding-left: 24px; margin-bottom: 21px; }
  .criteria-list li::before {
    content: ""; position: absolute; left: 0; top: 14px;
    width: 10px; height: 10px; border-radius: 50%; background: var(--bullet-ink);
  }
  .details {
    position: absolute; left: 52px; top: 817px; width: 790px;
    font-size: 20px; line-height: 24px;
  }
  .details .eligibility { margin-bottom: 39px; }
  .details .contact { margin-bottom: 27px; }
  .details .email { color: var(--link-yellow); }
  .credits { position: absolute; left: 52px; top: 1054px; width: 830px; font-size: 18px; line-height: 22px; }
</style>
</head>
<body>
<main class="flyer">
  <header class="hero">
    <div class="hero-portrait" role="img" aria-label="Black and white portrait of a woman looking downward"></div>
    <h1 class="headline">REQUEST FOR<br>STUDY PARTICIPANTS</h1>
    <p class="study-title">EFFICIENCY OF RESOURCES AVAILABLE TO SURVIVORS<br>OF INTIMATE PARTNER ABUSE</p>
  </header>

  <section class="criteria-band">
    <ul class="criteria-list">
      <li>Are you eighteen years of age or older?</li>
      <li>Have you been a victim of domestic violence?</li>
      <li>Have you sought assistance with abuse in the last 12 months?</li>
      <li>Are you still in contact with the person who abused you?</li>
      <li>Are you willing and open to discussing your experience with<br>abuse and your attempts to access services or resources?</li>
    </ul>
  </section>

  <section class="details">
    <p class="eligibility">If you answered YES to all of these questions, you may be eligible to participate in a<br>study to better understand the resources needed and services expected for survivors<br>of domestic violence.</p>
    <p class="contact">Please contact Dana Whitfield at 1(555) 014-2290 or via email<br><span class="email">survivorvoices.study@example.org</span> for additional information</p>
    <p class="compensation">Participants will be compensated for their time</p>
  </section>

  <footer class="credits">
    Principal Investigator: Dana Whitfield<br>
    Institutional Affiliation:&nbsp; Lakeshore State University, Dept. of Criminology, Law and Justice<br>
    Contact Address:&nbsp; Post Office Box 20415, Millbrook, IL, 60999
  </footer>
</main>
</body>
</html>
```